Brivo Packworks Website using Wix Platform

Project Overview:
Brivo Packworks is a supply chain company specializing in packaging and manufacturing services for CPG (Consumer Packaged Goods) brands and nutritional/dietary supplement companies. The company offers end-to-end solutions including packaging design, production, co-packing, and private labeling. The goal of this project is to create a professional, user-friendly website that showcases your expertise, builds trust with potential clients, and generates leads for your services.

Objectives:
Establish Brand Authority: Position Brivo Packworks as a leader in the packaging and manufacturing industry for CPG and nutritional products.
Lead Generation: Encourage visitors to contact you for quotes, consultations, or further information.
Professional User Experience: Ensure the website is easy to navigate, visually appealing, and mobile-friendly.
SEO & Conversion Optimization: Optimize the site for search engines to attract organic traffic and improve conversion rates.
Primary Audience:
CPG Brands: Companies in industries like food and beverage, personal care, and household products looking for packaging and manufacturing services.
Nutritional/Dietary Supplement Brands: Companies in the health and wellness industry needing specialized packaging and manufacturing services for supplements, including compliance with regulatory standards (GMP).
Secondary Audience:
Potential partners looking to collaborate on co-packing or private labeling.
Key Features & Functionality:
Responsive Design:

The website must be fully responsive, ensuring optimal viewing across all devices (desktops, tablets, mobile).
User-Centric Navigation:

A clean, intuitive navigation system that allows users to quickly access key pages such as Home, Services, About Us, Case Studies, FAQ, and Contact.
Lead Generation Forms:

Prominent CTAs (Calls to Action) throughout the website encouraging users to “Request a Quote”, “Get in Touch”, or “Learn More” about your services.
Contact Form: Simple form allowing potential clients to submit inquiries about your services.
SEO Optimization:

The site should be optimized for relevant keywords (e.g., “co-packing services for CPG,” “nutritional supplement packaging,” “custom packaging solutions”), including meta descriptions, headers, and on-page content.
Content Management System (CMS):

An easy-to-use CMS (like WordPress or Webflow) for easy content updates. This will allow you to make changes to your services, case studies, and other sections without requiring a developer.
Analytics Integration:

Google Analytics or a similar tool for tracking site visitors and performance metrics to make data-driven decisions on site improvements.
Site Structure & Content:
1. Home Page:
Hero Section with tagline, images or video of your services in action, and a clear CTA (e.g., “Request a Quote”).
Value Proposition: Short and compelling introduction to Brivo Packworks’s core services and advantages.
Overview of Services: Highlight your key offerings (e.g., Packaging Design, Co-packing, Nutritional Supplement Packaging, Private Labeling).
Client Logos/Testimonials: Social proof to establish credibility.
CTA Buttons: Throughout the page to drive conversions (e.g., “Get a Free Consultation”).
2. About Us Page:
Company Overview: Explain your mission, values, and commitment to quality.
Team Overview (Optional): Introduce key team members to humanize your company and build trust.
Core Values and Differentiators: Showcase what makes Brivo Packworks unique—sustainability practices, regulatory compliance, and industry expertise.
3. Services Pages (Separate Pages for Each Service):
Packaging & Design: Custom packaging solutions, materials, and design services for CPG brands.
Manufacturing & Assembly: Your end-to-end production process, assembly capabilities, and how you support both small and large-scale runs.
Nutritional & Dietary Supplement Packaging: Focus on specialized packaging for supplements, regulatory compliance (GMP), and certifications.
Private Labeling: Services for clients who wish to brand their own products using your packaging.
Each service page will include detailed descriptions, benefits, process information, and CTAs like “Get Started” or “Request a Quote”.
4. Case Studies / Portfolio Page:
Success Stories: Showcase in-depth case studies of past projects, especially successful partnerships with CPG or supplement brands.
Before & After Images: Display the difference your services have made for clients, especially in terms of packaging quality or branding improvements.
Client Testimonials: Additional customer feedback to strengthen your brand reputation.
5. FAQ Page:
Address common questions related to lead times, regulatory compliance, order quantities, and specific details for different industries (e.g., dietary supplements).
The format will be accordion-style or dropdowns for easy scanning.
6. Contact Us Page:
Contact Form: With fields for name, email, company, and inquiry details.
Location Information: Physical address, phone number, and working hours.
Map Integration: If relevant, integrate Google Maps to show your office location.
Social Media Links: Link to your company’s LinkedIn, Instagram, or other relevant platforms.

Target Market(s)

Startup CPG Brands, Supplement Brands, Nutrition Brands

Industry/Entity Type

Flexible Packaging, Contract Manufacturing, Supplement & Food Manufacturing

Coding

Coded - Design and coding required

Number of Pages Required

5+ page

Requirements
Must have
• Use our colors.
Nice to have
• https://tornap482.sitebuildhost.example/brivopackworks - www.ninefoldlane.example - www.pelkasnacks.example - thebrightmill.example

```html
<!DOCTYPE html>
<html lang="en">
<head>
<meta charset="utf-8">
<title>Brivo Packworks – Simplifying the Process</title>
<link href="https://fonts.googleapis.com/css2?family=Lexend:wght@300;400;500;600;700&display=swap" rel="stylesheet">
<style>
:root{
  --navy:#0b1a4a;
  --blue:#1aa3de;
  --green:#b3d335;
  --light:#f1f1f1;
  --field:#ececec;
  --ink:#222;
  --footer:#232323;
  --white:#fff;
}
*{box-sizing:border-box;margin:0;padding:0}
html,body{width:1200px;height:3842px;overflow:hidden}
body{font-family:"Lexend",sans-serif;color:var(--ink);background:var(--white);position:relative}
.abs{position:absolute}
.accent{color:var(--blue)}
.btn{display:inline-flex;align-items:center;justify-content:center;background:var(--green);color:var(--white);border-radius:30px;font-weight:600}

/* hero */
.hero{position:absolute;left:0;top:0;width:1200px;height:720px;overflow:hidden}
.hero-photo{position:absolute;inset:0;background:radial-gradient(ellipse at 50% 40%,#6d6253 0%,#4a4339 45%,#2e2a25 100%)}
.hero-shade{position:absolute;inset:0;background:rgba(20,18,15,.25)}
.hero-curve{position:absolute;left:0;bottom:0}
.brand{position:absolute;display:flex;align-items:center;gap:10px;color:var(--white);font-weight:400;letter-spacing:1px}
.brand-mark{width:22px;height:22px;background:var(--blue)}
.nav{position:absolute;left:463px;top:33px;display:flex;gap:8px}
.nav a{color:var(--white);text-decoration:none;font-size:15px;font-weight:500;padding:9px 18px;border-radius:22px;letter-spacing:.3px}
.nav a.active{background:var(--blue)}
.hero-title{position:absolute;top:245px;width:100%;text-align:center;color:var(--white);font-size:66px;font-weight:600;letter-spacing:.5px}
.hero-sub{position:absolute;top:341px;width:100%;text-align:center;color:var(--white);font-size:26px;font-weight:500;line-height:36px}
.hero-cta{position:absolute;left:476px;top:435px;width:248px;height:57px;font-size:19px}
.dots{display:flex;gap:8px;justify-content:center}
.dots span{width:11px;height:11px;border-radius:50%;background:var(--white)}
.hero .dots{position:absolute;top:619px;width:100%}
.hero .dots span.on{background:var(--blue)}

/* about */
.about-card{left:75px;top:790px;width:600px;height:485px;background:var(--light);border-radius:48px;padding:68px 30px}
.about-card h2{font-size:42px;font-weight:600;line-height:48px;color:var(--navy)}
.about-card p{margin-top:22px;font-size:16px;line-height:30px;font-weight:400}
.about-card .btn{margin-top:28px;width:183px;height:56px;font-size:20px}
.tile{position:absolute;border-radius:30px}
.t-warm{background:linear-gradient(135deg,#d9c5a8,#b59371)}
.t-paper{background:linear-gradient(135deg,#eceae6,#cfccc6)}

/* bands */
.band{position:absolute;left:0;width:1200px;background:var(--navy)}
.wave{position:absolute;left:0}
.sec-title{position:absolute;width:100%;text-align:center;font-size:44px;font-weight:600}
.sec-title.on-dark{color:var(--white)}
.sec-title.on-light{color:var(--navy)}

/* services */
.service{position:absolute;width:270px;text-align:center;color:var(--white);font-size:20px;font-weight:600;line-height:30px}
.service .circle{width:203px;height:203px;border-radius:50%;margin:0 auto 14px}
.service.active{color:var(--green)}
.service.active .circle{border:7px solid var(--green)}

/* testimonials */
.testi{top:2070px;width:513px;height:290px;background:var(--light);border-radius:48px;text-align:center;padding:26px 30px}
.testi .q{font-size:50px;font-weight:700;color:var(--navy);line-height:44px}
.testi p{font-size:20px;line-height:30px;margin-top:6px}
.testi .client{margin-top:14px;font-size:26px;font-weight:700;color:var(--navy)}
.testi .who{margin-top:10px;font-size:15px;font-weight:600;color:var(--blue);line-height:20px}
.testi-dots{position:absolute;top:2418px;width:100%}
.testi-dots span{background:var(--navy)}
.testi-dots span.on{background:var(--green)}

/* consultation */
.consult-text{position:absolute;top:2662px;width:100%;text-align:center;color:var(--white);font-size:16px}
.field{background:var(--white);border-radius:30px;font-size:14px;color:#333;padding-left:20px;display:flex;align-items:center}
.consult-input{position:absolute;left:290px;top:2712px;width:623px;height:56px}
.consult-btn{position:absolute;left:290px;top:2783px;width:623px;height:57px;font-size:20px}

/* contact */
.h-left{position:absolute;font-size:42px;font-weight:600;color:var(--navy)}
.cfield{position:absolute;background:var(--field);border-radius:28px;font-size:13px;font-weight:600;color:#333;padding:22px 24px 0}
.map{position:absolute;left:617px;top:3050px;width:510px;height:335px;border-radius:28px;background:linear-gradient(160deg,#e6efe6,#d9e8de 60%,#cfe3d6)}

/* footer */
.footer{position:absolute;left:0;top:3515px;width:1200px;height:327px;background:var(--footer);color:var(--white)}
.fcol{position:absolute;font-size:15px;line-height:31px}
.fcol h4{font-size:21px;font-weight:600;color:var(--green);margin-bottom:4px}
.copy{font-size:13px;line-height:25px}
.hours{display:grid;grid-template-columns:145px auto}
.contact-line{display:flex;gap:14px;align-items:flex-start}
.socials{display:flex;gap:20px;margin-top:16px}
.socials span{width:20px;height:20px;border-radius:50%;background:var(--white)}
</style>
</head>
<body>

<!-- HERO -->
<header class="hero">
  <div class="hero-photo" role="img" aria-label="Flat lay of printed stand-up coffee pouches"></div>
  <div class="hero-shade"></div>
  <div class="brand" style="left:75px;top:38px;font-size:26px"><span class="brand-mark"></span>BRIVO PACKWORKS</div>
  <nav class="nav">
    <a class="active">HOME</a><a>SERVICES</a><a>ABOUT US</a><a>CASE STUDIES</a><a>FAQ</a><a>CONTACT</a>
  </nav>
  <h1 class="hero-title">Simplifying the Process.</h1>
  <p class="hero-sub">We are a leader in the packaging and manufacturing industry<br>for CPG and nutritional products.</p>
  <a class="btn hero-cta">REQUEST A QUOTE</a>
  <div class="dots"><span class="on"></span><span></span><span></span><span></span></div>
  <svg class="hero-curve" width="1200" height="80" viewBox="0 0 1200 80">
    <path d="M0,0 Q600,110 1200,0 L1200,80 L0,80 Z" fill="#fff"/>
    <path d="M90,38 Q600,112 1110,38 Q600,128 90,38 Z" fill="#1aa3de"/>
  </svg>
</header>

<!-- ABOUT -->
<section>
  <div class="abs about-card">
    <h2>About<br><span class="accent">Brivo Packworks</span></h2>
    <p>Brivo Packworks is a family-owned business in Dallas, Texas, with extensive experience in manufacturing and regulatory compliance. We simplify the manufacturing process with step-by-step guidance and a friendly customer service team. Let's take brand to the next level!</p>
    <a class="btn">Read More</a>
  </div>
  <div class="tile t-warm" style="left:705px;top:790px;width:204px;height:283px" role="img" aria-label="Kraft takeaway boxes on a desk"></div>
  <div class="tile t-warm" style="left:922px;top:790px;width:205px;height:189px" role="img" aria-label="Hands folding a kraft box"></div>
  <div class="tile t-paper" style="left:705px;top:1086px;width:204px;height:189px" role="img" aria-label="Hand sketching packaging shapes"></div>
  <div class="tile t-paper" style="left:922px;top:992px;width:205px;height:283px" role="img" aria-label="Box dieline sketches on paper"></div>
</section>

<!-- SERVICES -->
<section>
  <svg class="wave" style="top:1350px" width="1200" height="80" viewBox="0 0 1200 80">
    <path d="M90,52 Q600,-16 1110,52 Q600,0 90,52 Z" fill="#1aa3de"/>
    <path d="M0,80 Q600,-10 1200,80 Z" fill="#0b1a4a"/>
  </svg>
  <div class="band" style="top:1428px;height:520px"></div>
  <svg class="wave" style="top:1890px" width="1200" height="80" viewBox="0 0 1200 80">
    <path d="M0,58 Q600,-20 1200,58 L1200,80 L0,80 Z" fill="#fff"/>
    <path d="M0,62 Q600,-30 1200,62 Q600,-12 0,62 Z" fill="#1aa3de"/>
  </svg>
  <h2 class="sec-title on-dark" style="top:1452px">Key Services <span class="accent">Offering</span></h2>
  <div class="service active" style="left:61px;top:1530px"><div class="circle" style="background:linear-gradient(135deg,#ece8e2,#c9b79d)" role="img" aria-label="Packaging design sketches"></div>Packaging<br>Design</div>
  <div class="service" style="left:331px;top:1536px"><div class="circle" style="background:linear-gradient(135deg,#d6a57a,#8c5a35)" role="img" aria-label="Hands packing a cardboard box"></div>Co-packing</div>
  <div class="service" style="left:600px;top:1536px"><div class="circle" style="background:linear-gradient(135deg,#b3c7da,#8fa9c2)" role="img" aria-label="Supplement pouch mockup"></div>Nutritional Supplement<br>Packaging</div>
  <div class="service" style="left:870px;top:1536px"><div class="circle" style="background:linear-gradient(135deg,#f5c534,#ef5d7a)" role="img" aria-label="Colourful private label product boxes"></div>Private Labeling</div>
</section>

<!-- TESTIMONIALS -->
<section>
  <h2 class="sec-title on-light" style="top:1988px">Client <span class="accent">Testimonials</span></h2>
  <div class="abs testi" style="left:75px">
    <div class="q">&#10078;</div>
    <p>"Major shoutout to Marcus Holloway, the best supply Chain CPG guru in the business, for helping me establish our product ."</p>
    <div class="client">Nuvo</div>
    <div class="who">Reid Calloway, Founder &amp; CEO at Nuvo</div>
  </div>
  <div class="abs testi" style="left:614px">
    <div class="q">&#10078;</div>
    <p>"I would like to acknowledge the efforts, encouragement, and advice of Marcus and other individuals that help to make the Straight Talk Foods launch happen."</p>
    <div class="client" style="font-size:20px;margin-top:8px">Straight Talk Foods</div>
    <div class="who" style="margin-top:6px">Tessa Vangelder, PhD President &amp; Founder,<br>Straight Talk Foods</div>
  </div>
  <div class="dots testi-dots"><span></span><span class="on"></span><span></span><span></span></div>
</section>

<!-- CONSULTATION -->
<section>
  <svg class="wave" style="top:2480px" width="1200" height="86" viewBox="0 0 1200 86">
    <path d="M90,52 Q600,-16 1110,52 Q600,0 90,52 Z" fill="#1aa3de"/>
    <path d="M0,86 Q600,-10 1200,86 Z" fill="#0b1a4a"/>
  </svg>
  <div class="band" style="top:2564px;height:352px"></div>
  <h2 class="sec-title on-dark" style="top:2592px">Get a Free <span class="accent">Consultation</span></h2>
  <p class="consult-text">Nemo enim ipsam voluptatem quia voluptas sit aspernatur aut odit aut fugit, sed quia consequuntur magni dolores.</p>
  <div class="field consult-input">Enter Name</div>
  <a class="btn consult-btn">Get a Free Consultation</a>
</section>

<!-- CONTACT & MAP -->
<section>
  <h2 class="h-left" style="left:73px;top:2970px">Contact <span class="accent">Us</span></h2>
  <h2 class="h-left" style="left:615px;top:2970px">Location <span class="accent">Map</span></h2>
  <div class="cfield" style="left:75px;top:3050px;width:249px;height:54px;padding-top:19px">Name</div>
  <div class="cfield" style="left:337px;top:3050px;width:249px;height:54px;padding-top:19px">Company</div>
  <div class="cfield" style="left:75px;top:3116px;width:511px;height:54px;padding-top:19px">Email Address</div>
  <div class="cfield" style="left:75px;top:3184px;width:511px;height:134px">Message</div>
  <a class="btn abs" style="left:75px;top:3330px;width:211px;height:55px;font-size:20px">Get In Touch</a>
  <div class="map" role="img" aria-label="Street map showing the office location"></div>
</section>

<!-- FOOTER -->
<svg class="wave" style="top:3440px" width="1200" height="78" viewBox="0 0 1200 78">
  <path d="M90,44 Q600,-16 1110,44 Q600,0 90,44 Z" fill="#1aa3de"/>
  <path d="M0,78 Q600,-8 1200,78 Z" fill="#232323"/>
</svg>
<footer class="footer">
  <div class="brand" style="left:74px;top:124px;font-size:24px"><span class="brand-mark" style="width:20px;height:20px"></span>BRIVO PACKWORKS</div>
  <p class="abs copy" style="left:74px;top:169px">Copyright © 2024 Brivo Packworks.<br>All rights reserved.</p>
  <div class="fcol" style="left:365px;top:48px">
    <h4>Quick Links</h4>
    Home<br>About Us<br>Services<br>Case Studies<br>FAQ<br>Contact Us
  </div>
  <div class="fcol" style="left:588px;top:48px">
    <h4>Contact Us</h4>
    <div class="contact-line"><span style="color:var(--green)">&#9679;</span><span style="line-height:25px;padding-top:3px">48 Larchmont Row Suite 210,<br>Denver 80202, United States</span></div>
    <div class="contact-line" style="margin-top:8px"><span style="color:var(--green)">&#9742;</span>(555) 014-2290</div>
    <div class="contact-line" style="margin-top:8px"><span style="color:var(--green)">&#9993;</span>hello@brivopackworks.example</div>
    <div class="socials" aria-label="Social media links"><span></span><span></span><span></span><span></span><span></span></div>
  </div>
  <div class="fcol" style="left:884px;top:48px">
    <h4>Hours</h4>
    <div class="hours">
      <span>Monday – Friday</span><span>8am- 6pm</span>
      <span>Saturday</span><span>8am- 4pm</span>
      <span>Sunday</span><span class="accent">Closed</span>
    </div>
  </div>
</footer>

</body>
</html>
```